Business Card Design

Plumbing business.
Looking for a simple but professional looking design.
There are two variations of the logo; white background and black background. The logo with the white background is the primary business logo.
Industry/Entity Type
Business
Contact Information for Business Card
Marcus Fenley
Owner/Licensed Plumber
0412 396 081
info@marcusfenleyplumbing.com.au
www.marcusfenleyplumbing.com.au
Lic. 63941
Look and feel
Each slider illustrates characteristics of the customer's brand and the style your logo design should communicate.

```html
<!DOCTYPE html>
<html lang="en">
<head>
<meta charset="utf-8">
<title>Marcus Fenley Plumbing – Business Card</title>
<link rel="stylesheet" href="https://fonts.googleapis.com/css2?family=Open+Sans:wght@400;600;700&display=swap">
<style>
  :root {
    --stage: #2b2b2b;
    --card: #f7f7f5;
    --card-back: #e9e9e9;
    --teal: #1ba1b0;
    --ink: #3b3b3b;
    --text-grey: #9a9a9a;
  }
  * { box-sizing: border-box; margin: 0; padding: 0; }
  html, body { width: 1200px; height: 900px; overflow: hidden; }
  body {
    background: var(--stage);
    font-family: "Open Sans", Arial, sans-serif;
    position: relative;
  }
  .card {
    position: absolute;
    width: 530px;
    height: 300px;
    box-shadow: 0 8px 24px rgba(0,0,0,.45);
    overflow: hidden;
  }

  /* Front: contact details */
  .card-front {
    left: 165px;
    top: 95px;
    background: var(--card);
  }
  .accent-band {
    position: absolute;
    left: 0; top: 0; bottom: 0;
    width: 14px;
    background: var(--teal);
  }
  .details {
    position: absolute;
    left: 44px;
    top: 52px;
  }
  .holder-name {
    font-weight: 700;
    font-size: 33px;
    line-height: 1;
    color: var(--teal);
    letter-spacing: .5px;
    text-transform: uppercase;
  }
  .holder-title {
    margin-top: 4px;
    font-size: 13px;
    color: var(--text-grey);
    text-transform: uppercase;
    letter-spacing: .3px;
  }
  .contact-list { list-style: none; margin-top: 18px; }
  .contact-list li {
    font-size: 18px;
    line-height: 25px;
    color: var(--text-grey);
  }
  .contact-list .phone { color: var(--teal); }
  .contact-list .licence {
    font-size: 13px;
    margin-top: 4px;
    line-height: 18px;
  }

  /* Back: business name */
  .card-back {
    left: 445px;
    top: 390px;
    width: 515px;
    background: var(--card-back);
  }
  .backdrop-photo {
    position: absolute;
    inset: 0;
    background:
      radial-gradient(ellipse 160px 140px at 48% 55%, #f6f6f6 0%, rgba(246,246,246,0) 100%),
      linear-gradient(180deg, #ececec 0%, #e3e3e3 70%, #d9d9d9 100%);
  }
  .brand {
    position: absolute;
    left: 0; right: 0; top: 0; bottom: 0;
    display: flex;
    align-items: center;
    justify-content: center;
    gap: 16px;
  }
  .brand-square {
    width: 48px;
    height: 48px;
    background: var(--teal);
    flex: none;
  }
  .brand-name {
    font-weight: 600;
    font-size: 28px;
    line-height: 1;
    color: var(--ink);
    white-space: nowrap;
  }
</style>
</head>
<body>
  <section class="card card-front" aria-label="Business card front">
    <div class="accent-band"></div>
    <div class="details">
      <h1 class="holder-name">Marcus Fenley</h1>
      <p class="holder-title">Owner/Licensed Plumber</p>
      <ul class="contact-list">
        <li class="phone">0412 396 081</li>
        <li class="email">info@marcusfenleyplumbing.com.au</li>
        <li class="web">www.marcusfenleyplumbing.com.au</li>
        <li class="licence">LIC. 63941</li>
      </ul>
    </div>
  </section>

  <section class="card card-back" aria-label="Business card back">
    <div class="backdrop-photo" role="img" aria-label="Faded photograph of a white bathroom fixture"></div>
    <div class="brand">
      <div class="brand-square"></div>
      <p class="brand-name">Marcus Fenley Plumbing</p>
    </div>
  </section>
</body>
</html>
```